Packaging Design

“Plim” is a brand for an innovative toothbrush product that never before available in the market. The main concepts of the brand are eco-friendly, economy, e-commerce and ecosystem. The detail for each concept are as following accordingly:

Eco-friendly - As far as the waste pollution as well as global warming are concerned, ordinary toothbrush is definitely one of the cause. The mission is to reduce plastic waste as much as possible while the brushing application remains unchanged. For couple of years of R&D, the solution is successfully discovered by the idea of head replacement to reduce the plastic waste up to 75 percents each time the head is replaced. Please have a look at the attached picture for reference.

Economy - As a matter of facts, the economic crisis is the problem for everyone in the country which is being most concerned. The objective is to help everyone to be able to have more money in their pocket while their oral care routine stays healthy and effectively. The replacement of the head is found to be the logical and practical solution to this issue which in turn leads to the saving of 49% in spending. Basically, everyone replaces a new toothbrush every 2 months or less because the bristle is worn out. Consequently, just replace the damage part and keep the handle for continuous use.

E-commerce - As a toothbrush manufacturer, the selling price for consumers at every designated retailer is a lot higher than the price originally due to the huge profit margin. However, consumer behavior is not the same as the olden days when online shopping has become more popular by being a new part of consumer’s lifestyle. To ensure that consumers can save on their purchases, the concept of B2C is implemented by selling only on e-commerce to remove the profit margins that has always been the reason of life difficulties or even the increasing inflation rate every now and then.

Ecosystem - From the 3 concepts earlier, it is a definite answer to achieve the ecosystem. The complete detail of this achievement will be delivered via email.

Please create the design using the given layout. This packaging consists of one toothbrush with head and 2 more replacement heads for your information. Should you need any additional information, please feel free to contact me at any time.

Let’s put our hands together for a better world. Thank you for joining the revolution.

```html
<!DOCTYPE html>
<html lang="en">
<head>
<meta charset="utf-8">
<title>Plim Toothbrush Pack – Front and Back Panels</title>
<link rel="stylesheet" href="https://fonts.googleapis.com/css2?family=Ubuntu:wght@700&display=swap">
<style>
  :root {
    --leaf-light: #a6d21e;
    --leaf-dark: #6aae14;
    --brand-blue: #064f9c;
    --paper: #ffffff;
  }
  html, body {
    margin: 0;
    padding: 0;
    width: 900px;
    height: 1200px;
    overflow: hidden;
    background: var(--paper);
  }
  .pack-sheet {
    display: block;
    width: 900px;
    height: 1200px;
  }
  .fill-light { fill: var(--leaf-light); }
  .fill-dark { fill: var(--leaf-dark); }
  .fill-paper { fill: var(--paper); }
  .badge-new {
    font-family: "Ubuntu", sans-serif;
    font-weight: 700;
    font-size: 64px;
    letter-spacing: 2px;
    fill: var(--paper);
  }
  .brand-name {
    font-family: "Ubuntu", sans-serif;
    font-weight: 700;
    font-size: 160px;
    fill: var(--brand-blue);
  }
  .brand-mark { fill: var(--leaf-dark); }
</style>
</head>
<body>
<svg class="pack-sheet" viewBox="0 0 1654 2205" preserveAspectRatio="none" xmlns="http://www.w3.org/2000/svg">
  <defs>
    <clipPath id="panel-clip">
      <rect x="188" y="157" width="564" height="1898" rx="55"/>
    </clipPath>
    <g id="panel-top">
      <g clip-path="url(#panel-clip)">
        <path class="fill-light" d="M188,157 H752 V360 Q380,560 188,947 Z"/>
        <circle class="fill-dark" cx="188" cy="157" r="230"/>
      </g>
      <rect class="fill-paper hang-slot" x="446" y="305" width="306" height="44" rx="22"/>
    </g>
    <g id="panel-bottom">
      <rect class="fill-light" x="188" y="1632" width="564" height="24"/>
      <g clip-path="url(#panel-clip)">
        <path class="fill-dark" d="M188,1960 A270,270 0 0 1 458,1690 H752 V2055 H188 Z"/>
      </g>
    </g>
  </defs>

  <g class="panel panel-left">
    <use href="#panel-top"/>
    <use href="#panel-bottom"/>
    <text class="badge-new" x="290" y="285" text-anchor="middle" transform="rotate(-45 290 262)">NEW</text>
    <g class="brand-lockup">
      <text class="brand-name" x="335" y="1380" text-anchor="middle" dominant-baseline="middle" transform="rotate(-90 335 1380)">Plim</text>
      <rect class="brand-mark" x="312" y="1560" width="44" height="44"/>
    </g>
  </g>

  <g class="panel panel-right">
    <use href="#panel-top" transform="translate(1658,0) scale(-1,1)"/>
    <use href="#panel-bottom" transform="translate(1658,0) scale(-1,1)"/>
    <text class="badge-new" x="1368" y="285" text-anchor="middle" transform="rotate(45 1368 262)">NEW</text>
    <g class="brand-lockup">
      <text class="brand-name" x="1353" y="1380" text-anchor="middle" dominant-baseline="middle" transform="rotate(-90 1353 1380)">Plim</text>
      <rect class="brand-mark" x="1330" y="1560" width="44" height="44"/>
    </g>
  </g>
</svg>
</body>
</html>
```